Indoor Gun Range Web Design Project

Create a professional bold indoor gun range website. Logo colors are white, red, and black. This is a very professional gun range. Please use high quality stock images if possible. Stay away from a lot of militia type photos. Use your best judgement on what to put as a main image and headline.

Here are some websites that I like for design.

http://www.pinebrookarsenal.example/
http://www.layoutbazaar.example/website-templates/51947.html
http://www.marigoldworks.example/

Target Market(s)

Men ages 25-65

Industry/Entity Type

Gun

Requirements
Must have
• Bold lettering, logo attached, exciting photos.
Should not have
• A lot of militia photos.

```html
<!DOCTYPE html>
<html lang="en">
<head>
<meta charset="utf-8">
<title>Steady Aim Indoor Gun Range</title>
<link href="https://fonts.googleapis.com/css2?family=Open+Sans:wght@400;600;700&family=PT+Sans:wght@400;700&display=swap" rel="stylesheet">
<style>
:root{
  --ink:#000;
  --panel:#050505;
  --red:#c8262b;
  --red-deep:#7a0b0d;
  --btn:#8e1518;
  --white:#fff;
  --paper:#f4f4f6;
  --footer:#2b2b2b;
  --footer-line:#3d3d3d;
  --muted:#a9a9a9;
  --card-red:#8a1418;
}
*{box-sizing:border-box;margin:0;padding:0}
html,body{width:911px;height:1200px;overflow:hidden;background:var(--ink)}
body{position:relative;font-family:"Open Sans",Arial,sans-serif;color:var(--white)}
.abs{position:absolute}

.header-art{left:0;top:0;width:911px;height:460px;
  background:radial-gradient(ellipse at 58% 5%,#e0301f 0%,#8d1410 22%,#3a0605 45%,transparent 70%),
             radial-gradient(ellipse at 96% 30%,#b3170f 0%,#4a0706 30%,transparent 55%),
             radial-gradient(ellipse at 50% 95%,#3a0505 0%,transparent 50%),#0c0202}
.brand{left:40px;top:58px;font-family:"PT Sans",Arial,sans-serif;font-weight:700;font-size:17px;line-height:19px;letter-spacing:.5px;color:var(--white);display:flex;align-items:center;gap:10px}
.brand-mark{width:14px;height:14px;border-radius:50%;background:var(--red)}

.search{left:650px;top:41px;display:flex}
.search-field{width:150px;height:18px;background:var(--white);color:#888;font-size:10px;padding:3px 6px}
.search-btn{width:50px;height:18px;background:var(--red-deep);color:var(--white);font-size:10px;text-align:center;line-height:18px}

.nav{left:298px;top:88px;width:573px;height:37px;background:rgba(0,0,0,.88);display:flex}
.nav a{color:var(--white);text-decoration:none;font-weight:700;font-size:11.5px;line-height:37px;text-align:center;border-left:1px solid #333;flex:auto}
.nav a:first-child{border-left:none}

.slider{left:34px;top:125px;width:837px;height:308px;border:3px solid var(--white);background:#000;overflow:hidden}
.thumb{position:absolute;top:0;height:302px}
.thumb-a{left:0;width:90px;background:linear-gradient(180deg,#000 0%,#2a2a2a 45%,#050505 100%)}
.thumb-b{left:90px;width:88px;background:linear-gradient(180deg,#000 20%,#6b2a14 50%,#1a0c06 70%,#000 100%)}
.thumb-c{left:178px;width:88px;background:linear-gradient(90deg,#000,#111)}
.hero{position:absolute;left:266px;top:0;width:565px;height:302px;background:radial-gradient(ellipse at 55% 40%,#b9b9b9 0%,#6a6a6a 30%,#2a2a2a 65%,#0b0b0b 100%)}
.arrow{position:absolute;left:12px;top:120px}
.caption{position:absolute;left:266px;top:262px;width:565px;height:36px;background:rgba(25,25,25,.8);display:flex;align-items:center;justify-content:space-between;padding:0 14px}
.caption-title{font-weight:700;font-size:15px}
.dots{display:flex;gap:4px}
.dots i{width:8px;height:8px;border-radius:50%;background:var(--white)}

.main{left:38px;top:460px;width:830px;height:498px;background:var(--panel);border:1px solid #1c1c1c}
.divider{left:627px;top:460px;width:2px;height:498px;background:#1e1e1e}
.heading{font-family:"PT Sans",Arial,sans-serif;font-weight:700;font-size:15px;text-transform:uppercase;height:30px;line-height:30px;padding-left:10px;background:linear-gradient(90deg,#3a0506,#150202 60%,transparent)}
.heading em{font-style:normal;color:var(--red)}
.copy{font-size:10.5px;line-height:14px}

.card{width:178px;height:195px;background:linear-gradient(180deg,var(--white),#e8e8ee);padding:8px}
.card-photo{width:160px;height:90px;background:linear-gradient(135deg,#e8e8e8,#8a8a8a 50%,#2a2a2a)}
.card-name{margin-top:8px;font-weight:700;font-size:10px;color:var(--card-red);padding-left:3px}
.card-text{font-size:10px;line-height:13px;color:var(--card-red);padding-left:3px}
.btn{display:inline-block;width:80px;height:20px;line-height:20px;background:var(--btn);color:var(--white);font-weight:700;font-size:9.5px;text-align:center;border:1px solid #b7292d}
.card .btn{margin-top:14px;margin-left:3px}

.review{display:flex;gap:12px}
.review-photo{width:78px;height:72px;border:1px solid var(--white);background:linear-gradient(135deg,#ddd,#555 55%,#111)}
.review-date{font-size:10.5px}
.review-name{font-size:10px;font-weight:700;color:var(--red)}
.review-text{font-size:10px;line-height:13px}
.faq-link{font-size:10.5px;color:var(--red);text-decoration:underline}

.footer{left:0;top:958px;width:911px;height:242px;background:var(--footer)}
.fcol-sep{top:958px;width:1px;height:130px;background:var(--footer-line)}
.f-head{font-size:13px;color:var(--white)}
.f-list{list-style:none;font-size:11px;line-height:20px;color:var(--muted)}
.social{display:grid;grid-template-columns:24px 24px;gap:6px}
.social i{width:22px;height:22px;background:#555}
.rule{left:24px;top:1148px;width:860px;height:1px;background:#444}
.copyright{left:642px;top:1165px;font-size:10px;color:var(--muted)}
</style>
</head>
<body>
<div class="abs header-art" role="img" aria-label="Red glowing target crosshair and tech circuit artwork"></div>

<div class="abs brand"><span class="brand-mark"></span><span>STEADY AIM<br>INDOOR GUN RANGE</span></div>

<div class="abs search"><div class="search-field">type word here</div><div class="search-btn">SEARCH</div></div>

<nav class="abs nav">
  <a href="#">MAIN PAGE</a><a href="#">ABOUT US</a><a href="#">GUNS RANGE</a><a href="#">REVIEW</a><a href="#">TESTIMONIALS</a><a href="#">CONTACT US</a>
</nav>

<section class="abs slider">
  <div class="thumb thumb-a" role="img" aria-label="Pistol muzzle close-up"></div>
  <div class="thumb thumb-b" role="img" aria-label="Antique flintlock pistol"></div>
  <div class="thumb thumb-c" role="img" aria-label="Dark firearm detail"></div>
  <div class="hero" role="img" aria-label="Silver pistol on diamond plate steel"></div>
  <svg class="arrow" width="24" height="72" viewBox="0 0 24 72"><polyline points="22,2 3,36 22,70" fill="none" stroke="#fff" stroke-width="2"/></svg>
  <div class="caption">
    <span class="caption-title">Water gun &#187;</span>
    <span class="dots"><i></i><i></i><i></i><i></i></span>
  </div>
</section>

<main class="abs main"></main>
<div class="abs divider"></div>

<h2 class="abs heading" style="left:40px;top:471px;width:500px">Welcome to mainpage of <em>Steady Aim</em></h2>
<div class="abs copy" style="left:53px;top:512px;width:545px">
  <p>Brightforge Webworks provides you the Search Engine Optimization making your website search engine friendly. So that the website can achieve top position and ranking in the Internet searches and thereby increasing the scope for the website to be found by customers. We here modify the site to improve the ranking by using the keywords and contents.</p>
  <p style="margin-top:14px">E-Commerce is a major progress in technology that has changed the way in which the customers now purchase information, products and the services. It's the new way of providing an opportunity to make your products and services available in the global market 24 hours a day through Internet<br>Brightforge Webworks is specialized in handling advanced web projects and the ongoing projects that require permanent maintenance and support .We like challenges and do complete these challenge with expertise we</p>
</div>

<h2 class="abs heading" style="left:38px;top:684px;width:520px">Latest <em>Editions</em></h2>

<article class="abs card" style="left:50px;top:735px">
  <div class="card-photo" role="img" aria-label="Silver semi-automatic pistol"></div>
  <p class="card-name">NAME OF GUN</p>
  <p class="card-text">Static website are the which are usually been used</p>
  <span class="btn">MORE INFO</span>
</article>
<article class="abs card" style="left:237px;top:735px">
  <div class="card-photo" role="img" aria-label="Rifle receiver close-up"></div>
  <p class="card-name">NAME OF GUN</p>
  <p class="card-text">Static website are the which are usually been used</p>
  <span class="btn">MORE INFO</span>
</article>
<article class="abs card" style="left:423px;top:735px">
  <div class="card-photo" role="img" aria-label="Rifle magazine and receiver"></div>
  <p class="card-name">NAME OF GUN</p>
  <p class="card-text">Static website are the which are usually been used</p>
  <span class="btn">MORE INFO</span>
</article>

<h2 class="abs heading" style="left:636px;top:468px;width:230px">Recent <em>Reviews</em></h2>
<div class="abs review" style="left:645px;top:512px">
  <div class="review-photo" role="img" aria-label="Pistol trigger close-up"></div>
  <div style="width:120px">
    <p class="review-date">December 25, 2011</p>
    <p class="review-name">GUN NAME</p>
    <p class="review-text">Brightforge Webworks provides you the Search Engine Optimization making your</p>
    <span class="btn" style="margin-top:8px;width:62px;height:16px;line-height:15px">MORE INFO</span>
  </div>
</div>
<div class="abs review" style="left:648px;top:638px">
  <div class="review-photo" role="img" aria-label="Rifle slide close-up"></div>
  <div style="width:118px">
    <p class="review-date">December 25, 2011</p>
    <p class="review-name">GUN NAME</p>
    <p class="review-text">Brightforge Webworks provides you the Search Engine Optimization making</p>
    <span class="btn" style="margin-top:8px;width:62px;height:16px;line-height:15px">MORE INFO</span>
  </div>
</div>

<h2 class="abs heading" style="left:633px;top:769px;width:233px">Support <em>FAQ</em></h2>
<div class="abs" style="left:646px;top:804px;width:210px">
  <p class="faq-link">YOUR GUN HEAD LINE HERE</p>
  <p class="copy" style="margin-top:4px">Brightforge Webworks provides you the Search Engine Optimization making your website search engine friendly.</p>
  <p class="copy" style="margin-top:14px">So that the website can achieve top position and ranking</p>
  <span class="btn" style="margin-top:14px">READ MORE</span>
</div>

<footer class="abs footer"></footer>
<div class="abs fcol-sep" style="left:313px"></div>
<div class="abs fcol-sep" style="left:628px"></div>

<div class="abs" style="left:48px;top:976px">
  <p class="f-head">Usefull&nbsp; Links</p>
  <div style="display:flex;gap:54px;margin-top:4px">
    <ul class="f-list"><li>About us</li><li>Why We Are</li><li>Why Choose Us</li><li>Testimonials</li><li>Contact Us</li></ul>
    <ul class="f-list"><li>Review</li><li>Recent News &amp; Blog</li><li>Branches &amp; Shop</li><li>Latest Edition</li></ul>
  </div>
</div>
<div class="abs" style="left:366px;top:975px">
  <p class="f-head">Gun Ranges</p>
  <ul class="f-list" style="margin-top:2px"><li>Most Popular gun</li><li>Best Awaited Range</li><li>High Ranges</li><li>Normal Ranges</li></ul>
</div>
<ul class="abs f-list" style="left:507px;top:992px"><li>&nbsp;Popular gun</li><li>Best Awaited Range</li><li>High Ranges</li><li>Normal Ranges</li></ul>
<div class="abs" style="left:682px;top:977px">
  <p class="f-head">Follow Us With</p>
  <div style="display:flex;gap:14px;margin-top:6px">
    <div class="social" style="margin-top:6px"><i></i><i></i><i></i><i></i></div>
    <ul class="f-list"><li>Circlebook</li><li>chirper</li><li>vidstream</li><li>workline</li></ul>
  </div>
</div>

<div class="abs rule"></div>
<p class="abs copyright">copyright &copy; 2012 Company Name&nbsp;&nbsp; All right reserved</p>
</body>
</html>
```